Tobias Wrenfield Business Card

In addition to my name design (file uploaded), black print on white card stock, e-mail address should be presented as a typical e-mail address, i.e., underlined and in blue ink, the card should include the following information:
Professor of Aviation Technology
Accident Litigation Expert Witness
Master Certificated Flight Instructor

twrenfield@qorvanet.net
Anchorage, Alaska
(907) 518-2736

Industry/Entity Type

Business

```html
<!DOCTYPE html>
<html lang="en">
<head>
<meta charset="utf-8">
<title>Tobias Wrenfield Business Card</title>
<link rel="stylesheet" href="https://fonts.googleapis.com/css2?family=Open+Sans:wght@400;800&display=swap">
<style>
  :root {
    --backdrop: #e9e9e7;
    --card: #ffffff;
    --ink: #231f20;
    --teal: #169a9c;
  }
  html, body {
    margin: 0;
    padding: 0;
    width: 1200px;
    height: 900px;
    overflow: hidden;
    background: var(--backdrop);
  }
  .card {
    position: absolute;
    left: 75px;
    top: 150px;
    width: 1050px;
    height: 600px;
    background: var(--card);
    box-shadow: 0 6px 24px rgba(0,0,0,0.12);
    font-family: "Open Sans", Arial, sans-serif;
    color: var(--ink);
  }
  .identity {
    position: absolute;
    right: 70px;
    top: 90px;
    text-align: right;
  }
  .name {
    margin: 0;
    font-weight: 800;
    font-size: 104px;
    line-height: 0.92;
    letter-spacing: -1px;
    text-transform: uppercase;
    color: var(--ink);
  }
  .roles {
    margin: 22px 0 0;
    padding: 0;
    list-style: none;
    font-weight: 400;
    font-size: 29px;
    line-height: 1.18;
  }
  .contact {
    position: absolute;
    left: 70px;
    bottom: 95px;
    color: var(--teal);
    font-weight: 400;
    font-size: 28px;
    line-height: 1.2;
  }
  .contact-pin {
    display: block;
    margin-left: 6px;
  }
  .contact-rule {
    width: 290px;
    height: 3px;
    background: var(--teal);
    margin: 4px 0 10px;
  }
  .contact p { margin: 0; }
</style>
</head>
<body>
  <div class="card">
    <div class="identity">
      <h1 class="name">Tobias<br>Wrenfield</h1>
      <ul class="roles">
        <li>Professor of Aviation Technology</li>
        <li>Accident Litigation Expert Witness</li>
        <li>Master Certificated Flight Instructor</li>
      </ul>
    </div>
    <div class="contact">
      <svg class="contact-pin" width="22" height="30" viewBox="0 0 22 30" aria-hidden="true">
        <path d="M11 0C4.9 0 0 4.9 0 11c0 8 11 19 11 19s11-11 11-19C22 4.9 17.1 0 11 0z" fill="var(--teal)"/>
        <circle cx="11" cy="11" r="4" fill="#ffffff"/>
      </svg>
      <div class="contact-rule"></div>
      <p class="contact-email">twrenfield@qorvanet.net</p>
      <p class="contact-city">Anchorage, Alaska</p>
      <p class="contact-phone">(907) 518-2736</p>
    </div>
  </div>
</body>
</html>
```